Modernise Business Card

Our company has been operating for 10 years. With the start of the new decade we are looking to refresh our business card design. We manufacture a range of industrial product shipping to customers internationally. A copy of our current card, both sides, is attached. We are looking for a mature professional appearance.

```html
<!DOCTYPE html>
<html lang="en">
<head>
<meta charset="utf-8">
<title>Korvane Business Card</title>
<link href="https://fonts.googleapis.com/css2?family=Source+Sans+3:wght@400;700&display=swap" rel="stylesheet">
<style>
  :root {
    --stage: #23272a;
    --card: #0c1b22;
    --card-edge: #0f222b;
    --brand-blue: #13a3dc;
    --brand-blue-deep: #0f87c0;
    --label-blue: #1e9fd6;
    --text-light: #e6ecef;
    --text-soft: #cfd6da;
  }
  * { margin: 0; padding: 0; box-sizing: border-box; }
  html, body {
    width: 1200px;
    height: 1176px;
    overflow: hidden;
    background: var(--stage);
    font-family: "Source Sans 3", sans-serif;
  }
  .card {
    position: absolute;
    left: 281px;
    width: 616px;
    height: 352px;
    border-radius: 20px;
    overflow: hidden;
    background: linear-gradient(135deg, var(--card) 0%, var(--card-edge) 100%);
  }
  .card--front { top: 190px; }
  .card--back { top: 591px; }

  .brand-panel {
    position: absolute;
    inset: 0;
    width: 616px;
    height: 352px;
  }
  .holder-name {
    position: absolute;
    left: 31px;
    top: 40px;
    font-size: 26px;
    font-weight: 400;
    color: var(--text-light);
    line-height: 1;
  }
  .name-rule {
    position: absolute;
    left: 31px;
    top: 84px;
    width: 47px;
    height: 2px;
    background: var(--brand-blue);
  }
  .contact-list {
    position: absolute;
    left: 31px;
    top: 99px;
    list-style: none;
  }
  .contact-item { margin-bottom: 8px; line-height: 18px; }
  .contact-label {
    display: block;
    font-size: 15px;
    color: var(--label-blue);
  }
  .contact-value {
    display: block;
    font-size: 15px;
    color: var(--text-light);
  }
  .address {
    position: absolute;
    left: 31px;
    top: 240px;
    font-style: normal;
    font-size: 15px;
    line-height: 23.5px;
    color: var(--text-soft);
  }
  .website {
    position: absolute;
    left: 380px;
    top: 318px;
    font-size: 15px;
    color: var(--text-light);
  }

  .wordmark {
    position: absolute;
    left: 0;
    right: 0;
    top: 138px;
    text-align: center;
    font-size: 72px;
    font-weight: 700;
    line-height: 80px;
    color: var(--brand-blue);
  }
  .product-lines {
    position: absolute;
    left: 0;
    right: 0;
    top: 272px;
    text-align: center;
    font-size: 15px;
    color: var(--text-light);
    word-spacing: 1px;
  }
  .product-lines .sep { margin: 0 10px; }
</style>
</head>
<body>
  <section class="card card--front">
    <svg class="brand-panel" viewBox="0 0 616 352" role="img" aria-label="Decorative brand colour panel">
      <defs>
        <linearGradient id="panelFill" x1="0" y1="0" x2="0" y2="1">
          <stop offset="0" stop-color="var(--brand-blue)"/>
          <stop offset="1" stop-color="var(--brand-blue-deep)"/>
        </linearGradient>
      </defs>
      <polygon points="218,352 447,0 616,0 616,352" fill="url(#panelFill)"/>
    </svg>
    <h1 class="holder-name">Ewan Hartley</h1>
    <div class="name-rule"></div>
    <ul class="contact-list">
      <li class="contact-item"><span class="contact-label">China:</span><span class="contact-value">+86 139 5520 7714</span></li>
      <li class="contact-item"><span class="contact-label">Australia:</span><span class="contact-value">+61 412 738 905</span></li>
      <li class="contact-item"><span class="contact-label">Email:</span><span class="contact-value">ehartley@korvanefittings.com</span></li>
    </ul>
    <address class="address">
      Lian Feng Building<br>
      114 Qiaolin Road, Haishu District<br>
      Ningbo 315000 China
    </address>
    <p class="website">www.korvanefittings.com</p>
  </section>

  <section class="card card--back">
    <p class="wordmark">Korvane</p>
    <p class="product-lines">Hydraulic Adapters<span class="sep">I</span>Hose Fittings<span class="sep">I</span>Quick Couplings</p>
  </section>
</body>
</html>
```